Verdant Medispa Business Card

need a business card for our medispa, attached please see the logo.
our website is https://verdantmedispa-example.com

Sorina Belcourt, MD
Internal Medicine

555-204-7193

Sorina@verdantmedispa-example.com

Www.Verdantmedispa-example.com

738 E Harlow Blvd N, Ste 512, Katy, TX 77981

Target Market(s)

MedSpa, Cosmetics, Esthetics

Industry/Entity Type

MedicalSpa

Contact Information for Business Card

Please see the attached business card which i pulled from the internet. I like the idea back as a logo and front with info.

Font styles to use
Decorative

Requirements
Must have
• Color should be matching with Logo and Website theme, Also I like to have QR code for the website

```html
<!DOCTYPE html>
<html lang="en">
<head>
<meta charset="utf-8">
<title>Verdant Medispa Business Card</title>
<link rel="stylesheet" href="https://fonts.googleapis.com/css2?family=Comfortaa:wght@400;500&family=Lato:wght@300;400&family=Yellowtail&display=swap">
<style>
  :root {
    --backdrop: #e7dccf;
    --card: #77614d;
    --gold: #c9a43c;
    --gold-soft: #a8873a;
    --ink: #f4eee6;
    --qr-tile: #efe6d6;
  }
  * { box-sizing: border-box; margin: 0; padding: 0; }
  html, body { width: 1200px; height: 771px; overflow: hidden; }
  body { background: var(--backdrop); position: relative; font-family: "Comfortaa", sans-serif; color: var(--ink); }

  .card {
    position: absolute;
    top: 255px;
    width: 454px;
    height: 295px;
    background: var(--card);
    box-shadow: 0 2px 6px rgba(60, 40, 20, 0.25);
    overflow: hidden;
  }
  .card--front { left: 108px; }
  .card--back { left: 643px; }

  /* Front */
  .front-brand {
    position: absolute;
    right: 14px;
    top: 20px;
    font-family: "Yellowtail", "Brush Script MT", cursive;
    font-size: 22px;
    color: var(--gold);
    line-height: 1;
    white-space: nowrap;
  }
  .icon {
    position: absolute;
    width: 22px;
    height: 22px;
    left: 13px;
  }
  .icon--person { width: 26px; height: 26px; left: 11px; top: 67px; }
  .icon--phone { top: 134px; }
  .icon--mail { top: 174px; }
  .icon--pin { top: 211px; }

  .person-name {
    position: absolute;
    left: 54px;
    top: 66px;
    font-family: "Yellowtail", "Brush Script MT", cursive;
    font-size: 24px;
    color: #fff;
    line-height: 1;
    white-space: nowrap;
  }
  .person-role {
    position: absolute;
    left: 54px;
    top: 99px;
    font-family: "Lato", sans-serif;
    font-weight: 300;
    font-size: 12.5px;
    letter-spacing: 0.4px;
  }
  .contact {
    position: absolute;
    left: 56px;
    font-size: 11.5px;
    line-height: 15px;
    white-space: nowrap;
  }
  .contact--phone { top: 138px; left: 57px; }
  .contact--mail { top: 178px; font-size: 10.5px; }
  .contact--address { top: 211px; left: 51px; }

  .floral-area {
    position: absolute;
    left: 292px;
    top: 120px;
    width: 148px;
    height: 175px;
  }

  /* Back */
  .back-brand {
    position: absolute;
    left: 0;
    right: 0;
    top: 78px;
    text-align: center;
    font-family: "Yellowtail", "Brush Script MT", cursive;
    font-size: 54px;
    color: var(--gold);
    line-height: 1.1;
    white-space: nowrap;
  }
  .back-web {
    position: absolute;
    left: 0;
    right: 0;
    top: 229px;
    text-align: center;
    font-family: "Lato", sans-serif;
    font-weight: 400;
    font-size: 9.5px;
    letter-spacing: 2.2px;
    text-transform: uppercase;
    color: var(--ink);
  }
  .qr-code {
    position: absolute;
    right: 18px;
    bottom: 18px;
    width: 46px;
    height: 46px;
  }
</style>
</head>
<body>

<section class="card card--front">
  <div class="front-brand">Verdant Medispa</div>

  <svg class="icon icon--person" viewBox="0 0 26 26" aria-hidden="true">
    <circle cx="13" cy="13" r="13" fill="var(--gold)"/>
    <circle cx="13" cy="10" r="4.2" fill="#fff"/>
    <path d="M5.5 20.5c1.2-4 4.2-5.6 7.5-5.6s6.3 1.6 7.5 5.6z" fill="#fff"/>
  </svg>
  <div class="person-name">Sorina Belcourt, MD</div>
  <div class="person-role">INTERNAL MEDICINE</div>

  <svg class="icon icon--phone" viewBox="0 0 22 22" aria-hidden="true">
    <circle cx="11" cy="11" r="11" fill="var(--gold)"/>
    <path d="M7.4 5.6l1.9-.4 1.2 2.9-1.3 1c.6 1.5 1.6 2.6 3.2 3.3l1-1.3 2.9 1.2-.4 1.9c-.2.7-.9 1-1.6.9-4-.8-6.8-3.6-7.6-7.6-.1-.7.2-1.4.7-1.9z" fill="#fff"/>
  </svg>
  <div class="contact contact--phone">555-204-7193</div>

  <svg class="icon icon--mail" viewBox="0 0 22 22" aria-hidden="true">
    <circle cx="11" cy="11" r="11" fill="var(--gold)"/>
    <rect x="5" y="7" width="12" height="8.5" rx="0.8" fill="#fff"/>
    <path d="M5.4 7.6L11 11.8l5.6-4.2" fill="none" stroke="var(--gold)" stroke-width="1"/>
  </svg>
  <div class="contact contact--mail">Sorina@verdantmedispa-example.com</div>

  <svg class="icon icon--pin" viewBox="0 0 22 22" aria-hidden="true">
    <circle cx="11" cy="11" r="11" fill="var(--gold)"/>
    <path d="M11 4.6a4.4 4.4 0 0 0-4.4 4.4c0 3.2 4.4 8.2 4.4 8.2s4.4-5 4.4-8.2A4.4 4.4 0 0 0 11 4.6z" fill="#fff"/>
    <circle cx="11" cy="9" r="1.7" fill="var(--gold)"/>
  </svg>
  <div class="contact contact--address">738 E Harlow Blvd N, Ste 512,<br>Katy, TX 77981</div>

  <svg class="floral-area" role="img" aria-label="Gold line-art floral vine decoration" viewBox="0 0 148 175" preserveAspectRatio="none">
    <defs>
      <radialGradient id="floral-tone" cx="0.55" cy="0.6" r="0.6">
        <stop offset="0" stop-color="var(--gold-soft)" stop-opacity="0.45"/>
        <stop offset="1" stop-color="var(--gold-soft)" stop-opacity="0"/>
      </radialGradient>
    </defs>
    <rect width="148" height="175" fill="url(#floral-tone)"/>
  </svg>
</section>

<section class="card card--back">
  <div class="back-brand">Verdant Medispa</div>
  <div class="back-web">Www.Verdantmedispa-example.com</div>
  <svg class="qr-code" role="img" aria-label="QR code linking to the website" viewBox="0 0 46 46">
    <rect width="46" height="46" rx="2" fill="var(--qr-tile)"/>
  </svg>
</section>

</body>
</html>
```